Building Company Business Card Design

I am looking to get a business card designed for my Building Company. Please find the logo attached.

Industry/Entity Type

Business

Contact Information for Business Card

Mobile 0472 913 046
Email admin@tarrowconstructworks.com.au
Website www.tarrowconstructworks.com.au

Colors
0255a3

```html
<!DOCTYPE html>
<html lang="en">
<head>
<meta charset="utf-8">
<title>Tarrow Construct Works – Business Card</title>
<link rel="stylesheet" href="https://fonts.googleapis.com/css2?family=Source+Sans+3:wght@600;700&display=swap">
<style>
  :root {
    --brand-blue: #0255a3;
    --slate: #53667d;
    --paper: #ffffff;
    --ink-grey: #5f6266;
  }
  * { margin: 0; padding: 0; box-sizing: border-box; }
  html, body {
    width: 1200px;
    height: 1200px;
    overflow: hidden;
    background: var(--paper);
    font-family: "Source Sans 3", "Myriad Pro", sans-serif;
  }
  .canvas { position: relative; width: 1200px; height: 1200px; }

  .card { position: absolute; width: 929px; height: 531px; overflow: hidden; }
  .card--front { left: 44px; top: 41px; }
  .card--back { left: 231px; top: 636px; background: var(--brand-blue); }

  .pattern-fill {
    position: absolute;
    background: linear-gradient(135deg, var(--brand-blue) 0%, var(--slate) 50%, var(--brand-blue) 100%);
  }
  .card--front .pattern-fill { inset: 0; }
  .pattern-fill--side { left: 0; top: 0; width: 187px; height: 100%; }
  .pattern-fill--edge { right: 0; top: 0; width: 17px; height: 100%; }

  .name-plate {
    position: absolute;
    left: 136px; top: 145px;
    width: 657px; height: 241px;
    background: var(--paper);
    border-radius: 121px;
    display: flex;
    align-items: center;
    justify-content: center;
    gap: 14px;
  }
  .wordmark {
    font-weight: 700;
    letter-spacing: 0.02em;
    text-transform: uppercase;
    white-space: nowrap;
  }
  .name-plate .wordmark { font-size: 44px; color: var(--brand-blue); }
  .name-plate .mark-dot {
    width: 18px; height: 18px; border-radius: 50%;
    background: var(--brand-blue);
  }

  .back-brand {
    position: absolute;
    right: 38px; top: 56px;
    display: flex; align-items: center; gap: 8px;
  }
  .back-brand .wordmark { font-size: 24px; color: var(--paper); }
  .back-brand .mark-dot {
    width: 9px; height: 9px; border-radius: 50%; background: var(--paper);
  }

  .contact {
    position: absolute;
    left: 228px; top: 330px;
    list-style: none;
    color: var(--paper);
    font-weight: 700;
  }
  .contact li { line-height: 1; white-space: nowrap; }
  .contact .phone { font-size: 31px; margin-bottom: 18px; }
  .contact .email,
  .contact .web { font-size: 27.5px; text-transform: uppercase; margin-bottom: 21px; }
</style>
</head>
<body>
<main class="canvas">
  <section class="card card--front">
    <div class="pattern-fill" role="img" aria-label="Blue and slate grey chevron stripe pattern"></div>
    <div class="name-plate">
      <span class="mark-dot"></span>
      <span class="wordmark">Tarrow Construct Works</span>
    </div>
  </section>

  <section class="card card--back">
    <div class="pattern-fill pattern-fill--side" role="img" aria-label="Blue and slate grey diagonal stripe pattern"></div>
    <div class="pattern-fill pattern-fill--edge" role="img" aria-label="Blue and slate grey diagonal stripe pattern"></div>
    <div class="back-brand">
      <span class="mark-dot"></span>
      <span class="wordmark">Tarrow Construct Works</span>
    </div>
    <ul class="contact">
      <li class="phone">0472 913 046</li>
      <li class="email">admin@tarrowconstructworks.com.au</li>
      <li class="web">www.tarrowconstructworks.com.au</li>
    </ul>
  </section>
</main>
</body>
</html>
```